New Business Card Design Project

We need to enhance the look and feel of our brand. We are starting with the business card and will hopefully expand to letter head, website, etc. The firm is based in Kolding Denmark and invests with global pension funds and for mutual fund investors alike. We would like to see an innovative use of the companies logo (star on the website - www.northmerrowcap.com) and a broader use of a color palette. Presently it is dominantly shades of blue. The firm wants to convey a sense they are a creative investment team that understands all the risks in the emerging markets and have the skills to perform in an environment of uncertainty.

Presently, we have three locations: Kolding Denmark, Glendale CA USA, Zurich Switzerland. We also have a prominently displayed bar code square on a solid dark blue back that will take smart phone users to the firm's website. I am indifferent to its inclusion., Details for my new Business Card Design Project will be added soon.
Updates

Project Deadline Extended
Reason: Designers, I am working with on getting feedback from both US and Danish partners on preferences. That is taking slightly more time than expected. Thanks for you patience. Nice work. TLV

Target Market(s)

The target market is a combination of institutional and retail investors. The european arm uses a card similar to a couple of those submitted.

Industry/Entity Type

Environment

Requirements
Must have
• The company's Star Logo. See www.northmerrowcap.com. It may be used in its current form or some new clever way. The founders are Danish and have a strong affinity for it.
Nice to have
• The new materials may be solely used in the north America and distributed in Australia as well. Therefore, we may try something new in these markets. I'd prefer to see a broader use of the color spectrum, not simply blue.
Should not have
• The card should not look and feel like a bank, insurance company, or a traditional money manager.

```html
<!DOCTYPE html>
<html lang="en">
<head>
<meta charset="utf-8">
<title>Northmerrow Business Card</title>
<link href="https://fonts.googleapis.com/css2?family=Roboto:wght@400;500;700&display=swap" rel="stylesheet">
<style>
  :root {
    --paper: #ffffff;
    --navy: #00289a;
    --cyan: #5ce3f8;
    --mark-ring: #4fdcf5;
    --white: #ffffff;
  }
  * { margin: 0; padding: 0; box-sizing: border-box; }
  html, body {
    width: 1050px;
    height: 1200px;
    overflow: hidden;
    background: var(--paper);
  }
  .card {
    width: 1050px;
    height: 1200px;
    display: flex;
    flex-direction: column;
    font-family: "Roboto", Arial, sans-serif;
  }
  .card-front {
    height: 600px;
    background: var(--paper);
    display: flex;
    align-items: center;
    justify-content: center;
    padding-bottom: 30px;
  }
  .brand {
    display: flex;
    align-items: center;
    gap: 26px;
  }
  .brand-dot { width: 90px; height: 90px; display: block; }
  .brand-name {
    font-size: 70px;
    font-weight: 500;
    color: var(--cyan);
    letter-spacing: 0.5px;
    line-height: 1;
  }
  .card-back {
    height: 600px;
    background: var(--navy);
    display: flex;
    flex-direction: column;
    align-items: center;
    padding-top: 177px;
    color: var(--white);
    text-align: center;
  }
  .person-name {
    font-size: 39px;
    font-weight: 700;
    line-height: 1.1;
  }
  .person-role {
    font-size: 31px;
    font-weight: 400;
    color: var(--cyan);
    margin-top: 4px;
  }
  .contact {
    margin-top: 40px;
    font-size: 31px;
    font-weight: 400;
    line-height: 1.3;
    letter-spacing: 0.3px;
  }
</style>
</head>
<body>
  <div class="card">
    <section class="card-front">
      <div class="brand">
        <svg class="brand-dot" viewBox="0 0 90 90" aria-hidden="true">
          <circle cx="45" cy="45" r="43" fill="var(--mark-ring)"/>
        </svg>
        <span class="brand-name">Northmerrow</span>
      </div>
    </section>
    <section class="card-back">
      <p class="person-name">Peter L. Harlow</p>
      <p class="person-role">Founder</p>
      <div class="contact">
        <p class="contact-email">pharlow@northmerrowcap.com</p>
        <p class="contact-phone">(+01)5550142873</p>
      </div>
    </section>
  </div>
</body>
</html>
```